ALL TEXT GRAPHICS TM May 2025 for Instagram

We are looking for a series of social media graphics for Instagram (new size: 4:5 (1080 x 1350 pixels) ratio that are ALL TEXT. We want the following quotes below on each graphic; one quote per graphic. AND, In very small letters at the bottom of each graphic, add @TovaMarshOnline
The look and feel of these graphics should be complimentary to the color palette attached below; but keep them simple. But the design is up to you; at the end of this document, I provided various samples of all text graphics that I like as examples.
Target Market(s)
women looking to lose weight
Look and feel

```html
<!DOCTYPE html>
<html lang="en">
<head>
<meta charset="utf-8">
<title>That Stubborn Weight – Instagram Quote</title>
<link rel="stylesheet" href="https://fonts.googleapis.com/css2?family=League+Gothic&family=Oswald:wght@300&family=Poppins:wght@600&family=Playfair+Display:wght@800&family=Great+Vibes&display=swap">
<style>
  :root {
    --pink: #d4006a;
    --ink: #363636;
    --paper: #ffffff;
  }
  html, body {
    margin: 0;
    padding: 0;
    width: 960px;
    height: 1200px;
    overflow: hidden;
    background: var(--paper);
  }
  .quote-card {
    display: block;
    width: 960px;
    height: 1200px;
  }
  .frame-line { stroke: var(--pink); stroke-width: 4.5; fill: none; }
  .callout-box { stroke: var(--pink); stroke-width: 1.6; stroke-dasharray: 1.6 2.6; fill: none; }
  .headline-top { font-family: "League Gothic", sans-serif; fill: var(--ink); }
  .headline-main { font-family: "League Gothic", sans-serif; fill: var(--pink); }
  .reassurance { font-family: "Oswald", sans-serif; font-weight: 300; fill: var(--ink); }
  .callout-text { font-family: "Poppins", sans-serif; font-weight: 600; fill: var(--pink); }
  .promise { font-family: "Playfair Display", serif; font-weight: 800; fill: var(--ink); }
  .handle { font-family: "Great Vibes", cursive; fill: #111111; }
</style>
</head>
<body>
<svg class="quote-card" viewBox="0 0 960 1200" xmlns="http://www.w3.org/2000/svg">
  <path class="frame-line" d="M278 1162 H52 V52 H907 V1162 H678"/>

  <text class="headline-top" x="150" y="267" font-size="178" textLength="642" lengthAdjust="spacingAndGlyphs">THAT STUBBORN</text>
  <text class="headline-main" x="147" y="562" font-size="366" textLength="709" lengthAdjust="spacingAndGlyphs">WEIGHT?</text>
  <text class="reassurance" x="226" y="667" font-size="52" textLength="498" lengthAdjust="spacingAndGlyphs">IT'S NOT YOUR FAULT.</text>

  <rect class="callout-box" x="181" y="708" width="585" height="214"/>
  <text class="callout-text" x="469" y="770" font-size="46" text-anchor="middle" textLength="432" lengthAdjust="spacingAndGlyphs">YOUR HORMONES</text>
  <text class="callout-text" x="470" y="830" font-size="46" text-anchor="middle" textLength="467" lengthAdjust="spacingAndGlyphs">ARE TO BLAME AND</text>
  <text class="callout-text" x="471" y="889" font-size="46" text-anchor="middle" textLength="470" lengthAdjust="spacingAndGlyphs">YOU'RE NOT ALONE;</text>

  <text class="promise" x="197" y="1016" font-size="66" textLength="569" lengthAdjust="spacingAndGlyphs">But there is a fix.</text>

  <text class="handle" x="479" y="1172" font-size="46" text-anchor="middle">@Tova Marsh Online</text>
</svg>
</body>
</html>
```